Business Card Design Project

1. Show the company logo.
2. Only company email ID and website address to be shown (office@tikhayavolna.fm , www.tikhayavolna.fm).
3. Logo to be provided by us, 2 designs just in case. The logo is made with ' Tikhaya Volna' text, need to be edited so that it shows 'Yasnaya Afisha' instead .
4. Single sided business card, portrait or landscape is not a problem; back side to be filled with colors or a design that matches the logo the best.
5. Logo is to be embossed.
6. We're looking at an English and Russian version.
7. any other better idea is always welcomed.

```html
<!DOCTYPE html>
<html lang="en">
<head>
<meta charset="utf-8">
<title>Business Card Design — Tikhaya Volna</title>
<link rel="stylesheet" href="https://fonts.googleapis.com/css2?family=Open+Sans:wght@400;700&family=Pathway+Gothic+One&display=swap">
<style>
  :root {
    --sheet-light: #ffffff;
    --sheet-dark: #bcbcbc;
    --card: #241f1d;
    --card-edge: #1a1614;
    --band-top: #3a3532;
    --band-mid: #2b2623;
    --band-bottom: #1d1917;
    --accent: #f2b705;
    --muted: #9a9591;
    --logo-blue: #123f86;
    --logo-rim: #d9dadb;
    --logo-text: #ffffff;
    --icon-bg: #141110;
    --icon-fg: #bdb8b4;
    --label-grey: #7a7a7a;
    --label-blue: #4b5472;
    --label-dark: #1c1c1c;
    --rule: #a9a9a9;
  }
  html, body {
    margin: 0;
    padding: 0;
    width: 1200px;
    height: 846px;
    overflow: hidden;
  }
  .sheet {
    position: relative;
    width: 1200px;
    height: 846px;
    background: radial-gradient(ellipse at 50% 35%, var(--sheet-light) 0%, #e6e6e6 45%, var(--sheet-dark) 100%);
    font-family: "Open Sans", Arial, sans-serif;
  }
  .card {
    position: absolute;
    width: 507px;
    height: 289px;
    background: var(--card);
    box-shadow: 2px 6px 10px rgba(0,0,0,0.35);
    overflow: hidden;
  }
  .card--front-en { left: 81px; top: 100px; }
  .card--front-ru { left: 640px; top: 100px; }
  .card--back { left: 81px; top: 455px; }
  .card__band {
    position: absolute;
    left: 0;
    width: 100%;
    top: 96px;
    height: 66px;
    background: linear-gradient(to bottom, var(--band-top) 0%, var(--band-mid) 30%, var(--band-bottom) 100%);
    border-top: 1px solid #4a4542;
    border-bottom: 1px solid #0f0c0b;
  }
  .card--back .card__band { height: 62px; }
  .logo {
    position: absolute;
    left: 50px;
    top: 34px;
    width: 186px;
    height: 186px;
  }
  .logo__disc {
    position: absolute;
    inset: 0;
    border-radius: 50%;
    background: var(--logo-blue);
    border: 4px solid var(--logo-rim);
    box-sizing: border-box;
  }
  .logo__name {
    position: absolute;
    left: 0;
    right: 0;
    top: 74px;
    text-align: center;
    color: var(--logo-text);
    font-weight: 700;
    font-size: 17px;
    line-height: 20px;
  }
  .player {
    position: absolute;
    left: 267px;
    top: 113px;
    display: flex;
    gap: 14px;
    align-items: center;
  }
  .player__button {
    width: 38px;
    height: 30px;
    background: var(--icon-bg);
    border-radius: 2px;
    display: flex;
    align-items: center;
    justify-content: center;
  }
  .player__slider { width: 48px; height: 10px; margin-left: -9px; }
  .contact {
    position: absolute;
    left: 267px;
    top: 172px;
  }
  .contact__web {
    color: var(--accent);
    font-weight: 700;
    font-size: 16px;
    line-height: 22px;
    margin: 0;
  }
  .contact__mail {
    color: var(--muted);
    font-size: 13px;
    line-height: 20px;
    margin: 0;
  }
  .card--back .contact__web {
    position: absolute;
    left: 55px;
    top: 118px;
    font-size: 14px;
  }
  .caption {
    position: absolute;
    left: 641px;
    top: 452px;
    width: 318px;
    font-family: "Pathway Gothic One", "Arial Narrow", sans-serif;
  }
  .caption__type {
    margin: 0 0 0 6px;
    font-size: 40px;
    line-height: 52px;
    color: var(--label-grey);
    font-weight: 400;
  }
  .caption__rule {
    height: 2px;
    background: var(--rule);
    margin: 28px 0 0 0;
    border: 0;
  }
  .caption__lead {
    margin: 14px 0 0 6px;
    font-size: 33px;
    line-height: 40px;
    color: var(--label-blue);
  }
  .caption__lead small { font-size: 24px; margin-left: 4px; }
  .caption__client {
    margin: 4px 0 0 6px;
    font-size: 44px;
    line-height: 52px;
    color: var(--label-dark);
    letter-spacing: 1px;
  }
  .caption__rule--lower { margin-top: 10px; }
</style>
</head>
<body>
<main class="sheet">

  <section class="card card--front-en" aria-label="Front, English version">
    <div class="card__band"></div>
    <div class="logo">
      <div class="logo__disc"></div>
      <div class="logo__name">Tikhaya<br>Volna</div>
    </div>
    <div class="player">
      <div class="player__button">
        <svg width="20" height="16" viewBox="0 0 20 16"><path d="M1 1 L10 8 L1 15 Z" fill="var(--icon-fg)"/><rect x="12" y="1" width="3" height="14" fill="var(--icon-fg)"/><rect x="16.5" y="1" width="3" height="14" fill="var(--icon-fg)"/></svg>
      </div>
      <div class="player__button">
        <svg width="20" height="16" viewBox="0 0 20 16"><path d="M1 5 H5 L10 1 V15 L5 11 H1 Z" fill="var(--icon-fg)"/><path d="M12 5 Q14 8 12 11 M14.5 3 Q18 8 14.5 13" stroke="var(--icon-fg)" stroke-width="1.5" fill="none"/></svg>
      </div>
      <svg class="player__slider" viewBox="0 0 48 10"><line x1="0" y1="5" x2="44" y2="5" stroke="#555" stroke-width="2"/><rect x="41" y="1" width="4" height="8" fill="var(--icon-fg)"/></svg>
    </div>
    <div class="contact">
      <p class="contact__web">www.tikhayavolna.fm</p>
      <p class="contact__mail">office@tikhayavolna.fm</p>
    </div>
  </section>

  <section class="card card--front-ru" aria-label="Front, alternate logo version">
    <div class="card__band"></div>
    <div class="logo">
      <div class="logo__disc"></div>
      <div class="logo__name">Yasnaya<br>Afisha</div>
    </div>
    <div class="player">
      <div class="player__button">
        <svg width="20" height="16" viewBox="0 0 20 16"><path d="M1 1 L10 8 L1 15 Z" fill="var(--icon-fg)"/><rect x="12" y="1" width="3" height="14" fill="var(--icon-fg)"/><rect x="16.5" y="1" width="3" height="14" fill="var(--icon-fg)"/></svg>
      </div>
      <div class="player__button">
        <svg width="20" height="16" viewBox="0 0 20 16"><path d="M1 5 H5 L10 1 V15 L5 11 H1 Z" fill="var(--icon-fg)"/><path d="M12 5 Q14 8 12 11 M14.5 3 Q18 8 14.5 13" stroke="var(--icon-fg)" stroke-width="1.5" fill="none"/></svg>
      </div>
      <svg class="player__slider" viewBox="0 0 48 10"><line x1="0" y1="5" x2="44" y2="5" stroke="#555" stroke-width="2"/><rect x="41" y="1" width="4" height="8" fill="var(--icon-fg)"/></svg>
    </div>
    <div class="contact">
      <p class="contact__web">www.tikhayavolna.fm</p>
      <p class="contact__mail">office@tikhayavolna.fm</p>
    </div>
  </section>

  <section class="card card--back" aria-label="Back">
    <div class="card__band"></div>
    <p class="contact__web">www.tikhayavolna.fm</p>
  </section>

  <aside class="caption">
    <h2 class="caption__type">Type B</h2>
    <hr class="caption__rule">
    <p class="caption__lead">Business Card Design <small>for</small></p>
    <h1 class="caption__client">TIKHAYA VOLNA</h1>
    <hr class="caption__rule caption__rule--lower">
  </aside>

</main>
</body>
</html>
```